32 x 24 Swinging Real Estate Yard Sign

We are looking to design a new sign for our business to focus on the remodeling of homes to sell. We are looking to have a yard sign that gets peoples attention and is informational. The headline will be "The Secret to Top Dollar? Remodel First.". We remodel homes for sellers with no up front cost, as they simply pay at closing. This link has more info, https://brightkeelhomes.com/Remodel
The message we want to convey to those seeing the sign is we are a one stop shop, who can renovate your home and sell it for no stress. We are licensed real estate agents and licensed contractors.
Both of these license numbers and info need to be on the design:
CADRE #07264918
Contractors License #2851736
Email: info@brightkeelhomes.com
Phone: (408)555-0183
I'll attach a sample sign we have for our agents normally as well as all brand art work.
• Pantone Colors
o #172A41
Dark blue
o #4381B1
Medium blue
o #6FA6CC
Light blue
Target Market(s)
Residential Real Estate Sellers
Industry/Entity Type
Real Estate
Colors
Designer to choose colors to be used in the design.

```html
<!DOCTYPE html>
<html lang="en">
<head>
<meta charset="utf-8">
<title>Brightkeel Homes Remodel Yard Sign</title>
<link rel="stylesheet" href="https://fonts.googleapis.com/css2?family=Montserrat:wght@500;600;700&family=Oswald:wght@700&display=swap">
<style>
  :root {
    --navy: #172A41;
    --blue-mid: #4381B1;
    --blue-light: #6FA6CC;
    --white: #FFFFFF;
    --backdrop: #E9ECEF;
  }
  * { margin: 0; padding: 0; box-sizing: border-box; }
  html, body {
    width: 1200px; height: 1200px; overflow: hidden;
    background: var(--backdrop);
  }
  .sign {
    position: absolute; left: 195px; top: 35px;
    width: 810px; height: 1130px;
    background: var(--navy);
    color: var(--white);
    font-family: "Montserrat", sans-serif;
  }
  .brand {
    position: absolute; left: 0; right: 0; top: 56px;
    display: flex; flex-direction: column; align-items: center;
  }
  .brand-dot {
    width: 72px; height: 72px; border-radius: 50%;
    background: var(--blue-mid);
    margin-bottom: 34px;
  }
  .brand-name { text-align: center; line-height: 1; font-weight: 600; }
  .brand-name .main { display: block; font-size: 74px; letter-spacing: 1px; color: var(--white); }
  .brand-name .sub {
    display: block; font-size: 26px; letter-spacing: 16px;
    margin-top: 18px; padding-left: 16px; color: var(--blue-mid);
  }
  .headline-box {
    position: absolute; left: 46px; top: 372px;
    width: 723px; height: 318px;
    border: 3px solid var(--white);
  }
  .headline { display: block; width: 100%; height: 198px; }
  .headline-phone {
    position: absolute; left: 0; right: 0; bottom: 0; height: 114px;
    background: var(--white); color: var(--navy);
    font-weight: 700; font-size: 78px; letter-spacing: -1px;
    display: flex; align-items: center; justify-content: center;
    line-height: 1;
  }
  .pitch {
    position: absolute; left: 46px; right: 46px; top: 730px;
    text-align: center;
  }
  .pitch-lead { font-weight: 600; font-size: 27px; line-height: 1.35; }
  .pitch-offer {
    margin-top: 16px;
    font-weight: 700; font-size: 33px; line-height: 1.2;
    color: var(--blue-light);
  }
  .contact {
    position: absolute; left: 70px; top: 994px;
    font-weight: 500; font-size: 27px; line-height: 1.45;
  }
  .licenses {
    position: absolute; left: 582px; top: 946px;
    color: var(--blue-mid);
    font-weight: 500; font-size: 17px; line-height: 1.3;
    text-transform: uppercase;
  }
  .licenses p + p { margin-top: 26px; }
</style>
</head>
<body>
  <div class="sign">
    <div class="brand">
      <div class="brand-dot"></div>
      <div class="brand-name">
        <span class="main">BRIGHTKEEL</span>
        <span class="sub">HOMES</span>
      </div>
    </div>

    <div class="headline-box">
      <svg class="headline" viewBox="0 0 717 198" aria-label="The Secret to Top Dollar? Remodel First.">
        <text x="358" y="80" text-anchor="middle" textLength="650" lengthAdjust="spacingAndGlyphs"
              font-family="Oswald, sans-serif" font-weight="700" font-size="64" fill="#FFFFFF">THE SECRET TO TOP DOLLAR?</text>
        <text x="358" y="178" text-anchor="middle" textLength="600" lengthAdjust="spacingAndGlyphs"
              font-family="Oswald, sans-serif" font-weight="700" font-size="92" fill="#6FA6CC">REMODEL FIRST.</text>
      </svg>
      <div class="headline-phone">(408)555-0183</div>
    </div>

    <div class="pitch">
      <p class="pitch-lead">One stop shop: we renovate your home<br>and sell it, stress free.</p>
      <p class="pitch-offer">No upfront cost. Pay at closing.</p>
    </div>

    <div class="contact">
      <p>info@brightkeelhomes.com</p>
      <p>brightkeelhomes.com/Remodel</p>
    </div>

    <div class="licenses">
      <p>CADRE #07264918</p>
      <p>Contractors<br>License #2851736</p>
    </div>
  </div>
</body>
</html>
```